Header and Full-Page Flyer needed for 2021 Lone Range Civic Builders Summit

Save the Date Flyer and Header needed for V-OrbMQ's 2021 Lone Range Civic Builders Summit. The Lone Range Civic Builders Summit is developed by Owners, for Owners (and other industry stakeholders.

DO NOT INCLUDE This in your design - for reference on design ideas only.
About the The Lone Range Civic Builders Summit:

Are you working within the boundaries of a smaller town mentality?
Do you feel stuck within your Big City limits?

The Lone Range Civic Builders Summit is where municipalities, counties, ISD's, and other public entities will come together to share what they know, and define what they want to know more about capital project planning design, delivery, and operations.

Font styles to use
Sans Serif

Requirements
Must have
• Lone Range Civic Builders Summit
Date: August 5, 2021
Location: San Antonio, TX

```html
<!DOCTYPE html>
<html lang="en">
<head>
<meta charset="utf-8">
<title>Lone Range Civic Builders Summit – Save the Date</title>
<link rel="stylesheet" href="https://fonts.googleapis.com/css2?family=Smokum&family=Montserrat:wght@500;600;700&family=Archivo:wght@500;800&display=swap">
<style>
  :root {
    --brand-blue: #3a53a0;
    --brand-green: #78c05a;
    --paper: #ffffff;
    --soft-grey: #e3e3e3;
    --logo-grey: #5a5a5a;
    --photo-dark: #3f3b3d;
    --photo-mid: #7d7068;
    --photo-warm: #b5957f;
  }
  html, body {
    margin: 0;
    padding: 0;
    width: 1200px;
    height: 1200px;
    overflow: hidden;
    background: var(--paper);
  }
  .flyer {
    display: block;
    width: 1200px;
    height: 1200px;
  }
  .organizer-name {
    font-family: "Montserrat", sans-serif;
    font-weight: 700;
    fill: var(--brand-blue);
  }
  .title-western {
    font-family: "Smokum", "Rye", serif;
    fill: var(--brand-blue);
  }
  .title-band-text {
    font-family: "Montserrat", sans-serif;
    font-weight: 600;
    fill: var(--paper);
    letter-spacing: 1px;
  }
  .event-detail {
    font-family: "Archivo", sans-serif;
    font-size: 31px;
    fill: var(--brand-blue);
  }
  .event-detail .label { font-weight: 500; }
  .event-detail .value { font-weight: 800; }
  .host-name {
    font-family: "Montserrat", sans-serif;
    font-weight: 500;
    fill: var(--logo-grey);
  }
</style>
</head>
<body>
<svg class="flyer" viewBox="0 0 1200 1200" xmlns="http://www.w3.org/2000/svg">
  <defs>
    <linearGradient id="audience-tones" x1="0" y1="0" x2="0.25" y2="1">
      <stop offset="0" stop-color="var(--photo-dark)"/>
      <stop offset="0.5" stop-color="var(--photo-mid)"/>
      <stop offset="1" stop-color="var(--photo-warm)"/>
    </linearGradient>
  </defs>

  <!-- Event photo area -->
  <rect class="event-photo" x="0" y="0" width="1200" height="1200" fill="url(#audience-tones)"
        role="img" aria-label="Photo of a speaker presenting on stage to a seated conference audience"/>

  <!-- Main white panel with curved blue edge -->
  <path class="panel-edge-blue" fill="var(--brand-blue)"
        d="M0,0 H710 C622,90 602,250 642,390 C692,560 662,735 540,845 C400,965 180,978 0,962 Z"/>
  <path class="panel-edge-grey" fill="var(--soft-grey)"
        d="M0,0 H672 C590,90 572,250 612,390 C662,560 632,725 512,830 C376,942 176,950 0,930 Z"/>
  <path class="panel-main" fill="var(--paper)"
        d="M0,0 H640 C566,90 548,250 590,390 C638,560 610,715 492,815 C360,925 170,932 0,902 Z"/>

  <!-- Bottom-right host corner -->
  <path class="corner-edge-blue" fill="var(--brand-blue)"
        d="M520,1200 C600,1090 760,1010 960,1002 C1080,996 1150,960 1200,912 V1200 Z"/>
  <path class="corner-edge-grey" fill="var(--soft-grey)"
        d="M560,1200 C642,1110 792,1040 980,1032 C1092,1026 1160,994 1200,958 V1200 Z"/>
  <path class="corner-main" fill="var(--paper)"
        d="M598,1200 C680,1126 812,1062 992,1056 C1100,1050 1166,1020 1200,994 V1200 Z"/>

  <!-- Organizer name (top left) -->
  <text class="organizer-name" x="61" y="110" font-size="34">Lone Range Civic</text>
  <text class="organizer-name" x="61" y="152" font-size="34">Builders Summit</text>

  <!-- Event title -->
  <text class="title-western" x="61" y="515" font-size="190"
        textLength="506" lengthAdjust="spacingAndGlyphs">LONE RANGE</text>
  <text class="title-western" x="61" y="598" font-size="92"
        textLength="511" lengthAdjust="spacingAndGlyphs">CIVIC BUILDERS</text>

  <rect class="title-band" x="59" y="606" width="513" height="74" fill="var(--brand-green)"/>
  <text class="title-band-text" x="315" y="662" font-size="56" text-anchor="middle">SUMMIT</text>

  <!-- Date and location -->
  <text class="event-detail" x="303" y="724" text-anchor="middle">
    <tspan class="label">Date: </tspan><tspan class="value">August 5, 2021</tspan>
  </text>
  <text class="event-detail" x="303" y="764" text-anchor="middle">
    <tspan class="label">Location: </tspan><tspan class="value">San Antonio,TX</tspan>
  </text>

  <!-- Host name (bottom right) -->
  <circle class="host-mark" cx="863" cy="1089" r="45" fill="var(--brand-blue)"/>
  <text class="host-name" x="930" y="1104" font-size="48">V-OrbMQ</text>
</svg>
</body>
</html>
```